Our Velvetline

I am developing a web site which sells preowned high end designer handbags and accessories. Some of the brands include: Corvane, Edmond Sarrelle & Velsa, to name a few. I am after a luxurious and high end feel.

Some brands I like that express this feel include: Astrel, Velsa, tinclosetly.com, purseswaporkeep.com

I am after a logo, business card, letterhead, with compliments, address label and envelope designs.
The business name is Our velvetline, and the website will be www.ourvelvetline.com.au. I have thoughts of using OVL as a logo or OUR velvetline.com.au

I don't want a large logo, it needs to blend in with the name in some way - or may not need an image at all, if the style of the font speaks to the brand.

Thank-you

Project Deadline Extended
Reason: I would like to give designers plenty of time to be able to submit a design.

Target Market(s)

Women, aged 25-60 who are into fashion

Industry/Entity Type

Business

Requirements
Must have
• High End
Luxurious

```html
<!DOCTYPE html>
<html lang="en">
<head>
<meta charset="utf-8">
<title>Our Velvetline — Stationery Set</title>
<link href="https://fonts.googleapis.com/css2?family=Arimo:wght@400;700&display=swap" rel="stylesheet">
<style>
  :root {
    --backdrop: #efece6;
    --paper: #ffffff;
    --gold: #ddd6a6;
    --gold-strip: #e6e0b6;
    --grey-strip: #e6e6e6;
    --grey-band: #d6d6d6;
    --grey-mark: #dcdcdc;
    --mark-faint: #f4f2e6;
    --mark-faint-square: #f1f1f1;
    --edge: #d9d9d9;
  }
  * { margin: 0; padding: 0; box-sizing: border-box; }
  html, body { width: 900px; height: 1200px; overflow: hidden; }
  body {
    position: relative;
    background: var(--backdrop);
    font-family: "Arimo", Arial, sans-serif;
  }

  /* Letterhead */
  .letterhead {
    position: absolute; left: 140px; top: 70px;
    width: 612px; height: 791px;
    background: var(--paper);
  }
  .letterhead__band-top {
    position: absolute; left: 0; top: 0; width: 100%; height: 18px;
    background: linear-gradient(90deg, #ffffff 0%, var(--grey-band) 100%);
  }
  .letterhead__band-rule {
    position: absolute; left: 0; top: 85px; width: 100%; height: 17px;
    background: linear-gradient(90deg, var(--grey-band) 0%, #f4f4f4 50%, var(--grey-band) 100%);
  }
  .letterhead__contact {
    position: absolute; left: 17px; top: 27px; width: 200px;
    font-size: 8.6px; font-weight: 700; line-height: 10.2px;
    color: var(--gold);
  }
  .letterhead__brand {
    position: absolute; left: 230px; top: 35px; height: 32px;
  }
  .letterhead__watermark {
    position: absolute; left: 106px; top: 353px; height: 86px;
  }
  .letterhead__footer-rule {
    position: absolute; left: 191px; top: 753px; width: 229px; height: 4px;
    background: linear-gradient(90deg, #f2f2f2 0%, #bdbdbd 100%);
  }
  .letterhead__footer-url {
    position: absolute; left: 0; top: 765px; width: 100%;
    text-align: center; font-size: 11.5px; font-weight: 700;
    color: var(--gold);
  }

  /* Brand name lockup */
  .brand {
    display: flex; align-items: center; gap: 8px;
    color: var(--gold); font-weight: 400; white-space: nowrap;
  }
  .brand__square { display: block; background: var(--grey-mark); flex: none; }
  .brand--small .brand__square { width: 32px; height: 32px; }
  .brand--small .brand__name { font-size: 15px; }
  .brand--faint { gap: 18px; color: var(--mark-faint); }
  .brand--faint .brand__square { width: 86px; height: 86px; background: var(--mark-faint-square); }
  .brand--faint .brand__name { font-size: 40px; }
  .brand--card .brand__square { width: 43px; height: 43px; }
  .brand--card .brand__name { font-size: 18px; }

  /* Envelope */
  .envelope {
    position: absolute; left: 165px; top: 915px;
    width: 372px; height: 190px;
    background: var(--paper);
    border: 1px solid var(--edge);
  }
  .envelope__flap { position: absolute; left: 0; top: 0; }
  .envelope__url {
    position: absolute; left: 98px; top: 12px;
    font-size: 9.5px; font-weight: 700; color: var(--gold);
  }

  /* Business card */
  .card {
    position: absolute; left: 360px; top: 945px;
    width: 375px; height: 190px;
    background: var(--paper);
    border: 1px solid var(--edge);
  }
  .card__strip-left {
    position: absolute; left: 17px; top: 0; width: 21px; height: 100%;
    background: var(--grey-strip);
  }
  .card__strip-right {
    position: absolute; left: 335px; top: 0; width: 20px; height: 100%;
    background: var(--gold-strip);
  }
  .card__brand {
    position: absolute; left: 86px; top: 74px;
  }
  .card__address {
    position: absolute; left: 90px; top: 126px;
    font-size: 9.5px; font-weight: 700; color: var(--gold);
  }
</style>
</head>
<body>

  <section class="letterhead" aria-label="Letterhead">
    <div class="letterhead__band-top"></div>
    <address class="letterhead__contact" style="font-style: normal;">
      Address: 128 Larkspur Avenue, Fernhill,<br>
      VIC 3999<br>
      Phone: 400-555-019<br>
      Fax: 400-555-019<br>
      Email: mara@ourvelvetline.com.au
    </address>
    <div class="letterhead__brand brand brand--small">
      <span class="brand__square"></span>
      <span class="brand__name">Our Velvetline</span>
    </div>
    <div class="letterhead__band-rule"></div>

    <div class="letterhead__watermark brand brand--faint" aria-hidden="true">
      <span class="brand__square"></span>
      <span class="brand__name">Our Velvetline</span>
    </div>

    <div class="letterhead__footer-rule"></div>
    <p class="letterhead__footer-url">www.ourvelvetline.com.au</p>
  </section>

  <section class="envelope" aria-label="Envelope">
    <svg class="envelope__flap" width="372" height="60" viewBox="0 0 372 60" aria-hidden="true">
      <polyline points="0,0 38,46 332,46 372,0" fill="none" stroke="#cfcfcf" stroke-width="1"/>
    </svg>
    <p class="envelope__url">www.ourvelvetline.com.au</p>
  </section>

  <section class="card" aria-label="Business card">
    <div class="card__strip-left"></div>
    <div class="card__strip-right"></div>
    <div class="card__brand brand brand--card">
      <span class="brand__square"></span>
      <span class="brand__name">Our Velvetline</span>
    </div>
    <p class="card__address">128 Larkspur Avenue, Fernhill, VIC 3999</p>
  </section>

</body>
</html>
```